Town Planning business needs a design (template) for planning reports and letters

I'm looking to develop a report and a letter template. I prepare town planning reports in NSW, Australia. Fairly straight forward reports which would include figures and tables. I can provide examples of similar reports. I have a logo design which I can also provide ( I have attached one file).

Target Market(s)

Professionals, local and state governments

Industry/Entity Type

Property Development

Requirements
Must have
• Title page, contents, 3 - 4 levels of headings, tables and ability to inset figures/photos and Annexure pages at end of report
Nice to have
• Ability to include short details of project in header or footer

```html
<!DOCTYPE html>
<html lang="en">
<head>
<meta charset="utf-8">
<title>Planning Report Template – Cover, Body and Data Pages</title>
<link href="https://fonts.googleapis.com/css2?family=Roboto:wght@400;500;700&family=Lato:wght@300;400&display=swap" rel="stylesheet">
<style>
  :root {
    --stage: #9e9e9e;
    --page: #f1f7fc;
    --brand: #0777bc;
    --heading: #0b74c0;
    --accent: #1aa3e8;
    --ink: #2b2f36;
    --footer: #1e2229;
    --row-alt: #ececec;
    --row: #f8f8f8;
    --dot-blue: #0b6fbd;
    --dot-grey: #9a9a9a;
    --dot-dark: #5a5a5a;
    --pie-dark: #5b5b5b;
    --pie-blue: #0679d2;
    --pie-light: #3db5f5;
    --pie-pale: #c6c6c6;
  }
  * { box-sizing: border-box; margin: 0; padding: 0; }
  html, body { width: 1200px; height: 576px; overflow: hidden; }
  body { background: var(--stage); position: relative; font-family: "Lato", sans-serif; }

  .page { position: absolute; top: 28px; width: 360px; height: 517px; background: var(--page); overflow: hidden; }
  .page--cover { left: 31px; }
  .page--body { left: 414px; }
  .page--data { left: 806px; }

  .page-footer {
    position: absolute; left: 0; right: 0; bottom: 0; height: 25px;
    background: var(--footer); color: #e6e6e6;
    font-family: "Roboto", sans-serif; font-size: 5.2px; line-height: 8px;
    text-align: center; padding-top: 5px; white-space: nowrap;
  }

  /* Cover */
  .cover-band { position: absolute; left: 0; top: 0; width: 100%; height: 387px; background: var(--brand); color: #fff; font-family: "Roboto", sans-serif; text-align: center; }
  .cover-rule { position: absolute; left: 61px; width: 240px; height: 1.5px; background: #fff; }
  .cover-rule--top { top: 162px; }
  .cover-rule--bottom { top: 235px; }
  .cover-title { position: absolute; top: 172px; width: 100%; font-size: 27px; font-weight: 700; letter-spacing: .2px; }
  .cover-subtitle { position: absolute; top: 203px; width: 100%; font-size: 17px; font-weight: 400; }
  .cover-meta { position: absolute; top: 251px; width: 100%; font-size: 11.5px; font-weight: 400; line-height: 16.5px; letter-spacing: .4px; }
  .cover-brand { position: absolute; top: 420px; left: 110px; display: flex; align-items: center; gap: 12px; }
  .cover-brand__square { width: 32px; height: 32px; background: var(--accent); }
  .cover-brand__name { font-family: "Roboto", sans-serif; font-weight: 700; font-size: 20px; line-height: 21px; color: var(--footer); letter-spacing: .5px; }

  /* Shared text */
  .page-brand { position: absolute; top: 12px; right: 12px; font-family: "Roboto", sans-serif; font-weight: 700; font-size: 7px; color: var(--accent); letter-spacing: .4px; }
  .heading-main { position: absolute; left: 11px; top: 23px; font-family: "Roboto", sans-serif; font-weight: 500; font-size: 17px; color: var(--heading); }
  .heading-accent { position: absolute; left: 0; top: 17px; width: 5px; height: 26px; background: var(--heading); }
  .heading-sub { position: absolute; left: 11px; font-family: "Roboto", sans-serif; font-weight: 500; font-size: 11px; color: var(--heading); }
  .body-copy { position: absolute; left: 11px; width: 338px; font-family: "Lato", sans-serif; font-weight: 300; font-size: 8.9px; letter-spacing: -0.05px; line-height: 13.7px; color: var(--ink); }

  .bullet-list { position: absolute; left: 12px; top: 291px; width: 340px; list-style: none; }
  .bullet-list li { position: relative; padding-left: 15px; font-weight: 300; font-size: 8.9px; letter-spacing: -0.05px; line-height: 13.7px; color: var(--ink); margin-bottom: 4.5px; }
  .bullet-list li::before { content: ""; position: absolute; left: 1px; top: 4px; width: 5px; height: 5px; background: var(--accent); }

  /* Table */
  .data-table { position: absolute; left: 11px; top: 153px; width: 335px; border-collapse: separate; border-spacing: 1.5px 0; font-family: "Roboto", sans-serif; font-size: 4.8px; line-height: 1; }
  .data-table th { background: var(--heading); color: #fff; font-size: 5.6px; font-weight: 500; height: 18px; padding: 0; text-align: center; }
  .data-table th:first-child { width: 82px; }
  .data-table td { height: 15.2px; padding: 0; text-align: center; background: var(--row); }
  .data-table tr:nth-child(odd) td { background: var(--row-alt); }
  .data-table td:first-child { text-align: left; padding-left: 12px; color: var(--ink); }
  .dot { display: inline-block; width: 4px; height: 4px; border-radius: 50%; background: var(--dot-blue); vertical-align: middle; }
  .dot--grey { background: var(--dot-grey); }
  .dot--dark { background: var(--dot-dark); }

  .donut { position: absolute; left: 187px; top: 314px; }
  .donut text { font-family: "Roboto", sans-serif; font-size: 11px; fill: #fff; text-anchor: middle; }
</style>
</head>
<body>

<section class="page page--cover">
  <div class="cover-band">
    <div class="cover-rule cover-rule--top"></div>
    <h1 class="cover-title">Project Title here</h1>
    <p class="cover-subtitle">Report sub details here</p>
    <div class="cover-rule cover-rule--bottom"></div>
    <p class="cover-meta">Persentator Name : ABC<br>Date: February 2023</p>
  </div>
  <div class="cover-brand">
    <span class="cover-brand__square"></span>
    <span class="cover-brand__name">FIELDLINE<br>PLANNING</span>
  </div>
  <footer class="page-footer">Lorem Ipsum is simply dummy text of the printing and typesetting industry. Lorem Ipsum has been the industry's standard dummy &nbsp;Lorem<br>Ipsum is simply dummy text of the printing and typesetting industry. Lorem Ipsum has been the industry's standard dummy</footer>
</section>

<section class="page page--body">
  <span class="page-brand">FIELDLINE</span>
  <span class="heading-accent"></span>
  <h2 class="heading-main">Main Heading Here</h2>
  <p class="body-copy" style="top:50px">Lorem Ipsum is simply dummy text of the printing and typesetting industry. Lorem Ipsum has been the industry's standard dummy text ever since the 1500s, when an unknown printer took a galley of type and scrambled it to make a type specimen book. It has survived not only five centuries, but also the leap into electronic typesetting, remaining essentially unchanged. It was popularised in the 1960s with the release of Linotrace sheets containing Lorem Ipsum passages, and more recently with desktop publishing software like Pressmark Layout including versions of Lorem Ipsum.</p>
  <h3 class="heading-sub" style="top:157px">Subheading Text Title here</h3>
  <p class="body-copy" style="top:175px">Lorem Ipsum is simply dummy text of the printing and typesetting industry. Lorem Ipsum has been the industry's standard dummy text ever since the 1500s, when an unknown printer took a galley of type and scrambled it to make a type specimen book. It has survived not only five centuries, but also the leap into electronic typesetting, remaining essentially unchanged. It was popularised in the 1960s with the r</p>
  <h3 class="heading-sub" style="top:270px">Bullet Points Text here</h3>
  <ul class="bullet-list">
    <li>Lorem Ipsum is simply dummy text of the printing and typesetting industry. Lorem Ipsum has been the industry's standard dummy</li>
    <li>Lorem Ipsum is simply dummy text of the printing and typesetting industry. Lorem Ipsum has been the industry's standard dummy</li>
    <li>Lorem Ipsum is simply dummy text of the printing and typesetting industry. Lorem Ipsum has been the industry's standard dummy</li>
    <li>Lorem Ipsum is simply dummy text of the printing and typesetting industry. Lorem Ipsum has been the industry's standard dummy</li>
    <li>Lorem Ipsum is simply dummy text of the printing and typesetting industry. Lorem Ipsum has been the industry's standard dummy</li>
  </ul>
  <footer class="page-footer">Lorem Ipsum is simply dummy text of the printing and typesetting industry. Lorem Ipsum has been the industry's standard dummy &nbsp;Lorem<br>Ipsum is simply dummy text of the printing and typesetting industry. Lorem Ipsum has been the industry's standard dummy</footer>
</section>

<section class="page page--data">
  <span class="page-brand">FIELDLINE</span>
  <h2 class="heading-main">Tabular Data</h2>
  <p class="body-copy" style="top:54px">Lorem Ipsum is simply dummy text of the printing and typesetting industry. Lorem Ipsum has been the industry's standard dummy text ever since the 1500s, when an unknown printer took a galley of type and scrambled it to &nbsp;Lorem Ipsum is simply dummy text of the printing and typesetting industry. Lorem Ipsum has been the industry's standard dummy text ever since the 1500s</p>
  <h3 class="heading-sub" style="top:137px;font-size:10px">Table Data Title Here</h3>
  <table class="data-table">
    <thead><tr><th>FEATURE DESCRIPTION</th><th>COLUMN TITLE</th><th>COLUMN TITLE</th><th>COLUMN TITLE</th><th>COLUMN TITLE</th></tr></thead>
    <tbody>
      <tr><td>First Row</td><td><span class="dot"></span></td><td><span class="dot"></span></td><td><span class="dot"></span></td><td><span class="dot"></span></td></tr>
      <tr><td>Second Row</td><td><span class="dot dot--grey"></span></td><td><span class="dot"></span></td><td><span class="dot"></span></td><td><span class="dot dot--grey"></span></td></tr>
      <tr><td>Third Row</td><td><span class="dot"></span></td><td><span class="dot dot--grey"></span></td><td><span class="dot"></span></td><td><span class="dot"></span></td></tr>
      <tr><td>Rowmance</td><td><span class="dot"></span></td><td><span class="dot dot--grey"></span></td><td><span class="dot"></span></td><td><span class="dot"></span></td></tr>
      <tr><td>Berow</td><td><span class="dot dot--dark"></span></td><td><span class="dot"></span></td><td><span class="dot dot--grey"></span></td><td><span class="dot"></span></td></tr>
      <tr><td>Rowanow</td><td><span class="dot dot--dark"></span></td><td><span class="dot"></span></td><td><span class="dot dot--grey"></span></td><td><span class="dot"></span></td></tr>
      <tr><td>Last Row</td><td><span class="dot"></span></td><td><span class="dot"></span></td><td><span class="dot dot--grey"></span></td><td><span class="dot"></span></td></tr>
    </tbody>
  </table>
  <h3 class="heading-sub" style="top:302px;font-size:10px">Pie Chart Design Content</h3>
  <p class="body-copy" style="top:318px;width:168px">Lorem Ipsum is simply dummy text of the printing and typesetting industry. Lorem Ipsum has been the industry's standard dummy text ever since the 1500s, when an unknown printer took a galley of type and scrambled it to.</p>
  <p class="body-copy" style="top:413px;width:168px">Lorem Ipsum is simply dummy text of the printing and typesetting industry. Lorem Ipsum has been the industry's standard dummy text ever</p>
  <svg class="donut" width="156" height="156" viewBox="0 0 156 156" role="img" aria-label="Donut chart of five segments">
    <g transform="rotate(-90 78 78)" fill="none" stroke-width="30">
      <circle cx="78" cy="78" r="62" pathLength="360" stroke="var(--pie-dark)" stroke-dasharray="60 300" stroke-dashoffset="35"/>
      <circle cx="78" cy="78" r="62" pathLength="360" stroke="var(--pie-blue)" stroke-dasharray="80 280" stroke-dashoffset="-25"/>
      <circle cx="78" cy="78" r="62" pathLength="360" stroke="var(--pie-pale)" stroke-dasharray="45 315" stroke-dashoffset="-105"/>
      <circle cx="78" cy="78" r="62" pathLength="360" stroke="var(--pie-blue)" stroke-dasharray="105 255" stroke-dashoffset="-150"/>
      <circle cx="78" cy="78" r="62" pathLength="360" stroke="var(--pie-light)" stroke-dasharray="70 290" stroke-dashoffset="-255"/>
    </g>
    <text x="80" y="24">20%</text>
    <text x="138" y="61">50%</text>
    <text x="133" y="121">20%</text>
    <text x="51" y="141">20%</text>
    <text x="21" y="62">40%</text>
  </svg>
  <footer class="page-footer">Lorem Ipsum is simply dummy text of the printing and typesetting industry. Lorem Ipsum has been the industry's standard dummy &nbsp;Lorem<br>Ipsum is simply dummy text of the printing and typesetting industry. Lorem Ipsum has been the industry's standard dummy</footer>
</section>

</body>
</html>
```